Rise Forward: Leave Behind Old Patterns, Quit Drifting Through Days, Begin Shaping each Morning

Good day! I am excited to work again with you, amazing designers! This time I am looking for the cover design of my book.
Dimensions 6” x 9”
The book name is as my name project. I love simplicity, but yet that is impactful. I love colours, I don't have a specific colour in mind, but I like the mustard colour as the one in the logo of my company. I am open to ideas! I have attached some cover samples that I like so that it gives a better idea of what I have on mind.
I am looking for something that looks professional, yet, not super serious, that it's approachable to people. Something that calls their attention at first glance.
I am working with my editor and my interior designer as well to finalize this part of the book. I will be working with the person that I select for the book design to finalize it.
About the book, here a passage of an unedited version of the introduction for guidance :
My intention is to take you on a journey to help you to understand what is going on in your mind so that you get out from anything that is holding you back in your life. My intention is to guide you to start fully living and experiencing a life that your mind even have yet conceived. To experience a life where you live fearless and without suffering. Living your life where you are the navigator and the creator of how you are experiencing it and you are living in a world of possibilities where there are no limitations.
For it, we will start to understand more about the mind and about the brain. I am not a neuroscientist and neither I consider my self an expert in the workings of the brain, what I know is the result of my fascination about our brain. This curiosity and the part of me that likes to understand how things work took me to read, research and learn about how our brain works and how its intrinsic mechanisms are subconsciously influencing and limiting us. I encourage you to stay on this part, it can be a bit technical, but understanding how it works will empower you not to allow your mind to dictate the way you approach your life and to live on autopilot.
We will continue to describe how you have been programmed throughout your life, putting you inside a box limited by your subconscious beliefs and ideas about the world. In this part, we will also discuss what ego is, how it is subconsciously limiting you and how the ways of when ego manifests itself are limiting you and making you suffer. Now that you know how you have been enclosed in your mind for all your life, we will move to discuss how you can get out of it. You will learn how to master your emotions to eliminate your suffering and not allow them to control the direction of your life and use them as a mechanism to get out from your programed mind. We continue to discuss how to leverage the power of your mind and harness your power of choice. Finally, I invite you to see yourself as a holistic being so that you start truly living and take control over the direction of your life, by nourishing and taking care of all those aspects of you utilizing their wisdom and synergy to achieve higher connection within yourself, your soul and live your life in a higher level of consciousness with peace, flow, love and purpose.

```html
<!DOCTYPE html>
<html lang="en">
<head>
<meta charset="utf-8">
<title>Rise Forward – Book Cover</title>
<link rel="stylesheet" href="https://fonts.googleapis.com/css2?family=Kaushan+Script&family=PT+Sans&family=Open+Sans:wght@600&display=swap">
<style>
  :root {
    --backdrop: #a679cf;
    --mustard: #e6b953;
    --maroon: #3d0b0e;
    --band: #2e0709;
    --cream: #f2e6cc;
    --art-deep: #26417e;
    --art-mid: #4a4fa8;
    --art-light: #7b5fb8;
  }
  * { box-sizing: border-box; margin: 0; padding: 0; }
  html, body {
    width: 1200px;
    height: 800px;
    overflow: hidden;
    background: var(--backdrop);
  }
  .canvas {
    position: relative;
    width: 1200px;
    height: 800px;
  }
  .cover {
    position: absolute;
    left: 360px;
    top: 40px;
    width: 480px;
    height: 720px;
    background: var(--mustard);
    overflow: hidden;
  }
  .cover__subtitle {
    position: absolute;
    top: 18px;
    left: 24px;
    right: 24px;
    font-family: "PT Sans", sans-serif;
    font-size: 15.5px;
    line-height: 20px;
    letter-spacing: 0.3px;
    text-align: center;
    color: var(--maroon);
  }
  .cover__title {
    position: absolute;
    top: 96px;
    left: 0;
    right: 0;
    font-family: "Kaushan Script", cursive;
    font-weight: 400;
    font-size: 72px;
    line-height: 1;
    text-align: center;
    color: var(--maroon);
  }
  .cover__swash {
    position: absolute;
    top: 186px;
    left: 250px;
    width: 200px;
    height: 30px;
  }
  .cover__art {
    position: absolute;
    left: 92px;
    top: 300px;
    width: 320px;
    height: 340px;
    border-radius: 28px;
    background: linear-gradient(160deg, var(--art-light) 0%, var(--art-mid) 45%, var(--art-deep) 100%);
  }
  .cover__author-band {
    position: absolute;
    left: 0;
    bottom: 0;
    width: 100%;
    height: 54px;
    background: var(--band);
    display: flex;
    align-items: center;
    justify-content: center;
  }
  .cover__author {
    font-family: "Open Sans", sans-serif;
    font-weight: 600;
    font-size: 28px;
    letter-spacing: 0.5px;
    color: var(--cream);
  }
</style>
</head>
<body>
  <main class="canvas">
    <section class="cover">
      <p class="cover__subtitle">Leave Behind Old Patterns, Quit Drifting Through Days,<br>Begin Shaping each Morning</p>
      <h1 class="cover__title">Rise Forward</h1>
      <svg class="cover__swash" viewBox="0 0 200 30" aria-hidden="true">
        <path d="M10 24 C 60 17, 130 11, 195 7" fill="none" stroke="var(--maroon)" stroke-width="4" stroke-linecap="round"/>
      </svg>
      <div class="cover__art" role="img" aria-label="Illustration of a calm figure with closed eyes whose hair is a cloud of colourful butterflies"></div>
      <footer class="cover__author-band">
        <span class="cover__author">Author Name</span>
      </footer>
    </section>
  </main>
</body>
</html>
```